PowerPoint Design Project

I need a Power Point slide template designed with 4 or 5 slides. We are a health care technology company and would like to take our current look and feel in this PP presentation to the next level and "prettied up"

Target Market(s)

Health Care Professionals

Industry/Entity Type

Health

Requirements
Must have
• Cannot change out the TREVONA logo. The logo is all CAPS
Should not have
• The color blue is restricted and cannot be used.

```html
<!DOCTYPE html>
<html lang="en">
<head>
<meta charset="utf-8">
<title>Trevona – Slide Template</title>
<link rel="stylesheet" href="https://fonts.googleapis.com/css2?family=Arimo:wght@400;700&display=swap">
<style>
  :root {
    --board: #c3c6ca;
    --paper: #ffffff;
    --olive: #9aad1c;
    --lime: #dde84e;
    --ink: #4a4a4a;
    --muted: #8e8e8e;
    --soft: #e8e7e3;
    --rule: #dcdcdc;
  }
  * { box-sizing: border-box; margin: 0; padding: 0; }
  html, body { width: 1200px; height: 944px; overflow: hidden; }
  body {
    background: var(--board);
    font-family: "Arimo", Arial, sans-serif;
    position: relative;
  }
  .slide {
    position: absolute;
    width: 521px;
    height: 391px;
    background: var(--paper);
    overflow: hidden;
    box-shadow: 0 2px 6px rgba(0,0,0,0.25);
  }
  .slide--cover { left: 61px; top: 52px; }
  .slide--infra { left: 618px; top: 52px; }
  .slide--personal { left: 61px; top: 498px; }
  .slide--treatment { left: 618px; top: 498px; }

  .brand {
    position: absolute;
    display: flex;
    align-items: center;
    gap: 8px;
    color: var(--muted);
    font-weight: 700;
    letter-spacing: 0.08em;
  }
  .brand-mark { background: var(--olive); display: block; }
  .brand--large { left: 55px; top: 84px; font-size: 33px; gap: 14px; }
  .brand--large .brand-mark { width: 26px; height: 26px; }
  .brand--small { right: 24px; top: 24px; font-size: 16px; }
  .brand--small .brand-mark { width: 12px; height: 12px; }

  .cover-glow {
    position: absolute; right: 0; top: 0; width: 260px; height: 230px;
    background: radial-gradient(ellipse at 100% 0%, var(--lime) 0%, rgba(221,232,78,0.45) 40%, rgba(255,255,255,0) 75%);
  }
  .side-rule { position: absolute; top: 0; bottom: 0; width: 1px; background: var(--rule); }
  .cover-title {
    position: absolute; left: 108px; top: 224px;
    color: var(--olive); font-size: 20px; font-weight: 700; line-height: 1.25;
    text-transform: uppercase; letter-spacing: 0.02em;
  }
  .cover-lead {
    position: absolute; left: 108px; top: 284px; width: 340px;
    color: var(--muted); font-size: 14px; font-weight: 700; line-height: 1.3;
  }
  .confidential { position: absolute; right: 20px; bottom: 20px; font-size: 5.5px; color: var(--muted); }

  .slide-title {
    position: absolute; left: 32px; top: 34px;
    color: var(--olive); font-size: 17px; font-weight: 700; line-height: 1.2;
    text-transform: uppercase; letter-spacing: 0.02em;
  }
  .decor { position: absolute; border-radius: 50%; background: var(--soft); }
  .bullets {
    position: absolute; left: 34px; top: 96px; width: 450px;
    list-style: none; color: var(--ink); font-size: 15px; line-height: 1.4;
  }
  .bullets li { position: relative; padding-left: 19px; margin-bottom: 6px; }
  .bullets li::before { content: "•"; position: absolute; left: 0; color: var(--olive); }
  .bullets .sub { font-size: 12.5px; line-height: 1.3; margin-left: 22px; color: #5a5a5a; }
  .page-num {
    position: absolute; left: 26px; bottom: 0; width: 21px; height: 21px;
    background: var(--olive); color: #fff; font-size: 7px;
    display: flex; align-items: center; justify-content: center;
  }
  .footer { position: absolute; bottom: 7px; font-size: 5.5px; font-style: italic; color: var(--muted); }
  .vertical-note {
    position: absolute; right: 6px; bottom: 20px;
    writing-mode: vertical-rl; transform: rotate(180deg);
    font-size: 5.5px; color: var(--muted);
  }
  .section-title {
    position: absolute; left: 43px; top: 90px;
    color: var(--olive); font-size: 17px; font-weight: 700; text-transform: uppercase; letter-spacing: 0.02em;
  }
  .section-lead {
    position: absolute; left: 43px; top: 122px; width: 250px;
    color: var(--muted); font-size: 14px; font-weight: 700; line-height: 1.3;
  }
</style>
</head>
<body>

<section class="slide slide--cover">
  <div class="cover-glow"></div>
  <div class="side-rule" style="left:92px"></div>
  <div class="brand brand--large"><span class="brand-mark"></span>TREVONA</div>
  <h1 class="cover-title">Better healthcare for a<br>better life</h1>
  <p class="cover-lead">Trevona as one of the world’s largest suppliers to the healthcare industry and a trendsetter in medical imaging, laboratory diagnostics, and medical information technology.</p>
  <p class="confidential">TREVONA Network Inc. Company Confidential.</p>
</section>

<section class="slide slide--infra">
  <div class="decor" style="left:322px; top:195px; width:240px; height:240px;"></div>
  <h2 class="slide-title">Healthcare infrastructure</h2>
  <div class="brand brand--small"><span class="brand-mark"></span>TREVONA</div>
  <ul class="bullets">
    <li>Quick access to all data generated by medical techniques significantly supports advanced hospital management.</li>
    <li>IT solutions provide important information in the right place at the right time and help to improve clinical and administrative processes as well as medical results.</li>
    <li class="sub">Hospital management systems that combine clinical, administrative, and financial components in one entity are known as HIS (Healthcare Information Systems).</li>
  </ul>
  <div class="page-num">2</div>
  <p class="footer" style="left:58px">Trevona, Company presentation. Better healthcare for a better life</p>
  <p class="vertical-note">TREVONA Network Inc. Company Confidential.</p>
</section>

<section class="slide slide--personal">
  <div class="side-rule" style="left:28px"></div>
  <div class="decor" style="left:252px; top:128px; width:300px; height:300px;"></div>
  <h2 class="section-title">Personalized healthcare</h2>
  <p class="section-lead">Provide accessible and affordable healthcare for everyone in Europe with S.M.A.R.T. products and high-quality refurbished systems.</p>
  <p class="footer" style="left:43px">Trevona, Company presentation. Better healthcare for a better life</p>
  <p class="vertical-note" style="right:14px">TREVONA Network Inc. Company Confidential.</p>
</section>

<section class="slide slide--treatment">
  <div class="decor" style="left:322px; top:200px; width:240px; height:240px;"></div>
  <h2 class="slide-title">Medical treatment and<br>equipment</h2>
  <div class="brand brand--small"><span class="brand-mark"></span>TREVONA</div>
  <ul class="bullets" style="top:92px">
    <li>Treatment is the attempted remediation of a health problem, usually following a diagnosis. Preventive treatments like vaccines are intended to prevent medical conditions like infectious diseases from occurring. An abortive treatment intends to stop a medical condition from progressing any further.</li>
  </ul>
  <div class="page-num">4</div>
  <p class="footer" style="left:58px">Trevona, Company presentation. Better healthcare for a better life</p>
  <p class="vertical-note">TREVONA Network Inc. Company Confidential.</p>
</section>

</body>
</html>
```